Heavy Equipment Service Technician

K&T Equipment Corp. is a family owned industry leader that’s been supplying construction equipment, tractors and landscaping gear to Southern Connecticut for the past 81 years. Located on Route 9 in Orange, we help home builders, site excavators, road builders, municipalities, landscapers, home owners and many more. We believe we can make work fun and easy by supplying new and used equipment, equipment rentals, service, parts and advice. Our fast paced service department is ready to expand! We are looking for a Heavy Equipment Service Technician, Experience Required.

QUALIFICATIONS AND SKILL:

· Must have a valid driver’s license.

· Must be reliable, hard working and have a professional work ethic.

· Must own tools and have the ability to work independently.

· Must have the ability to lift, push, pull 70+ pounds, climb heavy. equipment safely, bend and kneel.

· Must be able to perform basic equipment service: ie: filters, oils, inspections.

· Must possess a willingness to learn and grow.

· Must provide own tools.

RESPONSIBILITIES AND DUTIES:

· Perform scheduled services on heavy equipment and tractors.

· Perform final assembly of tractors.

· Perform body work on equipment.

· Perform minor welding on equipment and tractors.

· Keep work space clean of all debris.

Hi, This, is my first time using Mint Lantern! I am looking to design a new web page on our website that I can direct prospective employees. This webpage I want to look very professional to attract new employees. I am hoping to show off the wonderful benefits we offer, the fun work place and a great place to grow.

```html
<!DOCTYPE html>
<html lang="en">
<head>
<meta charset="utf-8">
<title>Careers – K&amp;T Equipment</title>
<link href="https://fonts.googleapis.com/css2?family=Montserrat:ital,wght@0,400;0,500;0,600;0,700;1,700&display=swap" rel="stylesheet">
<style>
:root{
  --ink:#111111;
  --text:#222222;
  --orange:#f7a823;
  --paper:#efefef;
  --white:#ffffff;
  --nav:#000000;
  --chat:#e8502a;
}
*{box-sizing:border-box;margin:0;padding:0}
html,body{width:1200px;height:2552px;overflow:hidden}
body{font-family:'Montserrat',sans-serif;color:var(--text);background:var(--paper);position:relative}
.site-header{height:152px;background:var(--white);position:relative}
.brand{position:absolute;left:95px;top:22px;display:flex;align-items:center;gap:12px}
.brand-dot{width:72px;height:72px;border-radius:50%;background:var(--orange)}
.brand-name{font-size:34px;font-weight:700;color:var(--ink);line-height:1}
.tagline{position:absolute;left:145px;top:122px;font-size:14px;color:#333}
.anniversary{position:absolute;left:560px;top:20px;width:95px;height:95px;border-radius:50%;background:var(--orange)}
.contact{position:absolute;right:90px;top:8px;text-align:right}
.phone{font-size:28px;font-weight:700;color:var(--ink);line-height:1.2}
.address{font-size:17px;font-weight:600;color:var(--ink)}
.social{display:flex;justify-content:flex-end;gap:10px;margin-top:6px}
.social span{width:32px;height:32px;background:var(--ink);border-radius:4px}
.search{margin-top:8px;margin-left:auto;width:163px;height:22px;border:1px solid #999;background:var(--white);position:relative}
.search svg{position:absolute;left:5px;top:3px}
.main-nav{height:54px;background:var(--nav);display:flex;justify-content:space-between;align-items:center;padding:0 20px}
.main-nav a{color:var(--white);font-size:10.5px;font-weight:700;text-decoration:none;letter-spacing:-.2px}
.hero{height:304px;border-bottom:3px solid var(--orange);background:linear-gradient(100deg,#8c8680 0%,#b9aa97 35%,#d7613a 55%,#6d6258 75%,#9b8d80 100%)}
.intro{width:960px;margin:68px auto 0;text-align:center;font-size:14.5px;line-height:26px}
.intro p+p{margin-top:10px}
.intro strong{font-weight:700;color:var(--ink)}
.section-title{text-align:center;font-size:24px;font-weight:700;color:var(--ink);letter-spacing:.3px}
.recruit-title{margin-top:82px;padding-left:16px}
.cards{display:flex;gap:28px;margin:35px 0 0 90px}
.card{width:500px;height:485px;border:2px solid var(--orange);padding:44px 18px 0 20px;background:rgba(255,255,255,.15)}
.card h3{text-align:center;font-size:23px;font-weight:500;color:var(--ink);margin-bottom:24px}
.ticks{list-style:none}
.ticks li{display:flex;gap:12px;font-size:14.5px;line-height:26px;margin-bottom:13px;padding-right:10px}
.ticks svg{flex:none;margin-top:5px}
.benefits-title{margin-top:92px}
.benefits{position:relative;height:560px;margin-top:36px}
.photo-frame{position:absolute;left:72px;top:14px;width:463px;height:489px;border:6px solid var(--orange)}
.photo{position:absolute;left:90px;top:0;width:457px;height:484px;background:linear-gradient(160deg,#9a9088 0%,#c7bfb5 40%,#d8532e 65%,#5b4b3e 100%)}
.perks{position:absolute;left:605px;top:0;width:520px}
.perk{display:flex;gap:24px;margin-bottom:20px}
.perk-icon{flex:none;width:90px;height:90px;border-radius:50%;background:var(--ink);display:flex;align-items:center;justify-content:center}
.perk h4{font-size:18px;font-weight:600;color:var(--ink);margin-top:4px;margin-bottom:4px}
.perk ul{list-style:none}
.perk li{position:relative;padding-left:16px;font-size:14.5px;line-height:26px;margin-bottom:6px}
.perk li::before{content:"";position:absolute;left:1px;top:11px;width:5px;height:5px;border-radius:50%;background:var(--orange)}
.fun-band{position:absolute;top:2107px;left:0;width:1200px;height:70px;background:var(--orange);display:flex;align-items:center;justify-content:center;font-size:25px;font-weight:700;font-style:italic;color:var(--ink)}
.partners{position:absolute;top:2268px;left:0;width:1200px;height:150px;background:var(--white);display:flex;align-items:center;justify-content:space-around;padding:0 260px 0 220px}
.partner{font-size:28px;font-weight:700;color:var(--ink);letter-spacing:1px}
.partner.orange{color:var(--chat)}
.text-us{position:absolute;right:34px;top:2350px;width:111px;height:42px;border-radius:21px;background:var(--chat);color:var(--white);font-size:14px;font-weight:700;display:flex;align-items:center;justify-content:center;gap:8px;box-shadow:0 2px 6px rgba(0,0,0,.3)}
.gallery{position:absolute;top:2418px;left:0;width:1200px;height:80px;display:flex}
.gallery div{flex:1;border-right:2px solid var(--white)}
.gallery div:nth-child(odd){background:linear-gradient(135deg,#b8b3ad,#d96a3a 60%,#6f6a64)}
.gallery div:nth-child(even){background:linear-gradient(135deg,#8e9aa6,#c9552e 55%,#5e6a5b)}
.site-footer{position:absolute;top:2498px;left:0;width:1200px;height:54px;background:var(--white);text-align:center;padding-top:32px;font-size:15px;color:#333}
</style>
</head>
<body>
<header class="site-header">
  <div class="brand"><span class="brand-dot"></span><span class="brand-name">K&amp;T Equipment</span></div>
  <div class="tagline">Sales, Service &amp; Rentals</div>
  <div class="anniversary" role="img" aria-label="81 years anniversary badge"></div>
  <div class="contact">
    <div class="phone">203-555-0148</div>
    <div class="address">52 Harbor Mill Road, Orange, CT 06477</div>
    <div class="social" aria-label="Social links"><span></span><span></span></div>
    <div class="search"><svg width="14" height="14" viewBox="0 0 14 14"><circle cx="5.5" cy="5.5" r="4" fill="none" stroke="#111" stroke-width="1.6"/><path d="M8.5 8.5L13 13" stroke="#111" stroke-width="1.8"/></svg></div>
  </div>
</header>
<nav class="main-nav">
  <a href="#">HOME</a><a href="#">NEW EQUIPMENT</a><a href="#">GENERATORS</a><a href="#">USED EQUIPMENT</a><a href="#">ATTACHMENTS</a><a href="#">RENTALS</a><a href="#">PARTS</a><a href="#">SERVICE</a><a href="#">SALES</a><a href="#">ABOUT US</a><a href="#">CONTACT US</a><a href="#">CAREERS</a>
</nav>
<div class="hero" role="img" aria-label="Technician operating an orange backhoe loader on a job site"></div>

<section class="intro">
  <p>K&amp;T Equipment Corp. is a family owned industry leader that’s been supplying construction equipment, tractors and landscaping gear to Southern Connecticut for the past 81 years. Located on Route 9 in Orange, we help home builders, site excavators, road builders, municipalities, landscapers, home owners and many more. We believe we can make work fun and easy by supplying new and used equipment, equipment rentals, service, parts and advice.</p>
  <p><strong>Our fast paced service department is ready to expand!</strong><br>We are looking for a Heavy Equipment Service Technician, Experience Required.</p>
</section>

<h2 class="section-title recruit-title">EMPLOYEE RECRUITMENT AND BENEFITS</h2>
<div class="cards">
  <div class="card">
    <h3>Qualifications And Skill</h3>
    <ul class="ticks">
      <li><svg width="17" height="17" viewBox="0 0 17 17"><circle cx="8.5" cy="8.5" r="7.5" fill="none" stroke="#f7a823" stroke-width="1.3"/><path d="M5 8.8l2.4 2.3 4.6-4.8" fill="none" stroke="#f7a823" stroke-width="1.4"/></svg>Must have a valid driver’s license.</li>
      <li><svg width="17" height="17" viewBox="0 0 17 17"><circle cx="8.5" cy="8.5" r="7.5" fill="none" stroke="#f7a823" stroke-width="1.3"/><path d="M5 8.8l2.4 2.3 4.6-4.8" fill="none" stroke="#f7a823" stroke-width="1.4"/></svg>Must be reliable, hard working and have a professional work ethic.</li>
      <li><svg width="17" height="17" viewBox="0 0 17 17"><circle cx="8.5" cy="8.5" r="7.5" fill="none" stroke="#f7a823" stroke-width="1.3"/><path d="M5 8.8l2.4 2.3 4.6-4.8" fill="none" stroke="#f7a823" stroke-width="1.4"/></svg>Must own tools and have the ability to work independently.</li>
      <li><svg width="17" height="17" viewBox="0 0 17 17"><circle cx="8.5" cy="8.5" r="7.5" fill="none" stroke="#f7a823" stroke-width="1.3"/><path d="M5 8.8l2.4 2.3 4.6-4.8" fill="none" stroke="#f7a823" stroke-width="1.4"/></svg>Must have the ability to lift, push, pull 70+ pounds, climb heavy. equipment safely, bend and kneel.</li>
      <li><svg width="17" height="17" viewBox="0 0 17 17"><circle cx="8.5" cy="8.5" r="7.5" fill="none" stroke="#f7a823" stroke-width="1.3"/><path d="M5 8.8l2.4 2.3 4.6-4.8" fill="none" stroke="#f7a823" stroke-width="1.4"/></svg>Must be able to perform basic equipment service: ie: filters, oils, inspections.</li>
      <li><svg width="17" height="17" viewBox="0 0 17 17"><circle cx="8.5" cy="8.5" r="7.5" fill="none" stroke="#f7a823" stroke-width="1.3"/><path d="M5 8.8l2.4 2.3 4.6-4.8" fill="none" stroke="#f7a823" stroke-width="1.4"/></svg>Must possess a willingness to learn and grow.</li>
      <li><svg width="17" height="17" viewBox="0 0 17 17"><circle cx="8.5" cy="8.5" r="7.5" fill="none" stroke="#f7a823" stroke-width="1.3"/><path d="M5 8.8l2.4 2.3 4.6-4.8" fill="none" stroke="#f7a823" stroke-width="1.4"/></svg>Must provide own tools.</li>
    </ul>
  </div>
  <div class="card">
    <h3>Responsibilities And Duties</h3>
    <ul class="ticks">
      <li><svg width="17" height="17" viewBox="0 0 17 17"><circle cx="8.5" cy="8.5" r="7.5" fill="none" stroke="#f7a823" stroke-width="1.3"/><path d="M5 8.8l2.4 2.3 4.6-4.8" fill="none" stroke="#f7a823" stroke-width="1.4"/></svg>Perform scheduled services on heavy equipment<br>and tractors.</li>
      <li><svg width="17" height="17" viewBox="0 0 17 17"><circle cx="8.5" cy="8.5" r="7.5" fill="none" stroke="#f7a823" stroke-width="1.3"/><path d="M5 8.8l2.4 2.3 4.6-4.8" fill="none" stroke="#f7a823" stroke-width="1.4"/></svg>Perform final assembly of tractors.</li>
      <li><svg width="17" height="17" viewBox="0 0 17 17"><circle cx="8.5" cy="8.5" r="7.5" fill="none" stroke="#f7a823" stroke-width="1.3"/><path d="M5 8.8l2.4 2.3 4.6-4.8" fill="none" stroke="#f7a823" stroke-width="1.4"/></svg>Perform body work on equipment.</li>
      <li><svg width="17" height="17" viewBox="0 0 17 17"><circle cx="8.5" cy="8.5" r="7.5" fill="none" stroke="#f7a823" stroke-width="1.3"/><path d="M5 8.8l2.4 2.3 4.6-4.8" fill="none" stroke="#f7a823" stroke-width="1.4"/></svg>Perform minor welding on equipment and tractors.</li>
      <li><svg width="17" height="17" viewBox="0 0 17 17"><circle cx="8.5" cy="8.5" r="7.5" fill="none" stroke="#f7a823" stroke-width="1.3"/><path d="M5 8.8l2.4 2.3 4.6-4.8" fill="none" stroke="#f7a823" stroke-width="1.4"/></svg>Keep work space clean of all debris.</li>
    </ul>
  </div>
</div>

<h2 class="section-title benefits-title">K&amp;T EQUIPMENT CORP EMPLOYEE BENEFITS</h2>
<div class="benefits">
  <div class="photo-frame"></div>
  <div class="photo" role="img" aria-label="Employee driving an orange compact wheel loader in a yard"></div>
  <div class="perks">
    <div class="perk">
      <div class="perk-icon"><svg width="40" height="40" viewBox="0 0 40 40" fill="none" stroke="#fff" stroke-width="2"><path d="M20 5l12 5v9c0 8-5 13-12 16C13 32 8 27 8 19v-9z"/><path d="M14 20l4 4 8-8"/></svg></div>
      <div><h4>Insurance Benefits</h4><ul>
        <li>Employer Paid, no cost Comprehensive Health Insurance</li>
        <li>Employer Paid, Short Term Disability Insurance</li>
        <li>Optional Dental, Vision, Long Term Disability, Hospitalization and Life Insurance</li></ul></div>
    </div>
    <div class="perk">
      <div class="perk-icon"><svg width="42" height="42" viewBox="0 0 42 42" fill="none" stroke="#fff" stroke-width="2"><rect x="6" y="9" width="26" height="24" rx="2"/><path d="M6 15h26M12 5v7M26 5v7"/><circle cx="31" cy="30" r="7" fill="#111"/><path d="M31 26v4h3"/></svg></div>
      <div><h4>Paid Time Off Benefits</h4><ul>
        <li>Paid Vacation Time (up to 2 weeks based on tenure)</li>
        <li>5 Paid Holidays per year</li>
        <li>5 Paid Covid Sick Days</li></ul></div>
    </div>
    <div class="perk">
      <div class="perk-icon"><svg width="40" height="40" viewBox="0 0 40 40" fill="none" stroke="#fff" stroke-width="2"><path d="M6 14L20 6l14 8H6zM9 16v13M16 16v13M24 16v13M31 16v13M5 33h30"/></svg></div>
      <div><h4>Retirement Benefits</h4><ul>
        <li>Elective Deferral pre-tax Simple IRA with 100% Employer Match (up to 3% of employee salary)</li></ul></div>
    </div>
  </div>
</div>

<div class="fun-band">"FUN AT WORK"</div>
<div class="partners">
  <span class="partner orange">Terrafield</span>
  <span class="partner">IRONVALE</span>
</div>
<div class="text-us"><svg width="18" height="16" viewBox="0 0 18 16"><path d="M1 1h16v10H7l-4 4v-4H1z" fill="#fff"/></svg>Text Us!</div>
<div class="gallery" role="img" aria-label="Row of equipment inventory photos">
  <div></div><div></div><div></div><div></div><div></div><div></div><div></div><div></div><div></div><div></div><div></div>
</div>
<footer class="site-footer">Copyright © 2022 K&amp;T Equipment. All Rights Reserved.</footer>
</body>
</html>
```